Business Card Design for Event Planning Company

Create a business card for event planning company using our new logo. After I pick the design, I will need files made for 6 employees. Our company provides event design & logistics services as well as venue management. The font should be sans serif and complementary to the logo. I will need to know the name of the font selected for the final design. The phone numbers listed should be separated by "." not "-"

Address for the card
PO Box 318, Washington, DC 20019

Card One
Lorna Pettibone
lpettibone@galavoyant.com
202.481.7730

Card Two
Miriam Okonkwo
mokonkwo@galavoyant.com
202.556.2047

Card Three
Tessa Varnholt
tvarnholt@galavoyant.com
978.620.4471

Card Four
Robin Fess
rfess@galavoyant.com
202.718.3362

Card Five
Ada-Rose Pelletan-Uzor
adarose@galavoyant.com
202.839.1205

Card Six
Beatrix Holloway
Beatrix@galavoyant.com
202.492.6618

Target Market(s)

Corporate/Non-Profit

Industry/Entity Type

Event Planning

Contact Information for Business Card

Address for the card

Card One
Lorna Pettibone
lpettibone@galavoyant.com
202.481.7730

Card Two
Miriam Okonkwo
202.556.2047

Card Three
Tessa Varnholt
978.620.4471

Card Four
Robin Fess
rfess@galavoyant.com
202.718.3362

Card Five
Ada-Rose Pelletan-Uzor
202.839.1205

Card Six
Beatrix Holloway
202.492.6618

Font styles to use
Sans Serif

Colors

Designer to choose colors to be used in the design.

Requirements
Must have
• Two-sided with logo
Should not have
• Extra colors or be too busy

```html
<!DOCTYPE html>
<html lang="en">
<head>
<meta charset="utf-8">
<title>galavoyant — business card</title>
<link rel="stylesheet" href="https://fonts.googleapis.com/css2?family=Montserrat:wght@600&family=Questrial&display=swap">
<style>
  :root {
    --teal: #5fa3a0;
    --teal-deep: #4e9390;
    --ink: #231815;
    --paper: #ffffff;
    --backdrop: #eeeeec;
    --edge: #9a9a9a;
  }
  * { margin: 0; padding: 0; box-sizing: border-box; }
  html, body { width: 1200px; height: 927px; overflow: hidden; }
  body {
    background: var(--backdrop);
    font-family: "Questrial", sans-serif;
    position: relative;
  }
  .card {
    position: absolute;
    left: 240px;
    width: 720px;
    height: 400px;
    overflow: hidden;
  }
  /* front */
  .card--front {
    top: 40px;
    background: var(--teal);
    border-radius: 0 58px 0 58px;
  }
  .front-brand {
    position: absolute;
    left: 0; right: 0;
    top: 190px;
    text-align: center;
    font-size: 60px;
    line-height: 1;
    color: var(--paper);
    letter-spacing: 0.5px;
  }
  .front-url {
    position: absolute;
    left: 0; right: 0;
    top: 286px;
    text-align: center;
    font-size: 23px;
    color: var(--paper);
  }
  /* back */
  .card--back {
    top: 487px;
    background: var(--paper);
    border: 1px solid var(--edge);
    border-radius: 58px 0 58px 0;
  }
  .holder-name {
    position: absolute;
    left: 62px;
    top: 90px;
    font-family: "Montserrat", sans-serif;
    font-weight: 600;
    font-size: 40px;
    line-height: 1;
    letter-spacing: 0.5px;
  }
  .holder-name .first { color: var(--teal); }
  .holder-name .last { color: var(--ink); }
  .contact-list {
    position: absolute;
    left: 62px;
    top: 180px;
    list-style: none;
  }
  .contact-list li {
    display: flex;
    align-items: center;
    height: 38px;
    font-size: 21px;
    color: var(--ink);
  }
  .contact-list svg {
    width: 20px;
    height: 20px;
    margin-right: 14px;
    flex: none;
  }
  .back-brand {
    position: absolute;
    left: 455px;
    top: 195px;
    display: flex;
    align-items: center;
    font-size: 34px;
    color: var(--teal);
  }
  .back-brand .mark-dot {
    width: 22px;
    height: 22px;
    border-radius: 50%;
    background: var(--ink);
    margin-right: 12px;
  }
  .address-band {
    position: absolute;
    left: 102px;
    width: 516px;
    bottom: 0;
    height: 52px;
    background: var(--ink);
    border-radius: 16px 16px 0 0;
    color: var(--paper);
    font-size: 20px;
    display: flex;
    align-items: center;
    justify-content: center;
  }
</style>
</head>
<body>

  <section class="card card--front" aria-label="Card front">
    <div class="front-brand">galavoyant</div>
    <div class="front-url">www.galavoyant.com</div>
  </section>

  <section class="card card--back" aria-label="Card back">
    <h1 class="holder-name"><span class="first">LORNA</span> <span class="last">PETTIBONE</span></h1>

    <ul class="contact-list">
      <li>
        <svg viewBox="0 0 20 20" aria-hidden="true">
          <rect x="6" y="2" width="8" height="16" rx="1.5" fill="none" stroke="var(--teal)" stroke-width="1.6"/>
          <line x1="9" y1="15.5" x2="11" y2="15.5" stroke="var(--teal)" stroke-width="1.6"/>
        </svg>
        202.481.7730
      </li>
      <li>
        <svg viewBox="0 0 20 20" aria-hidden="true">
          <rect x="2" y="5" width="16" height="11" fill="var(--teal)"/>
          <polyline points="2,5 10,11 18,5" fill="none" stroke="var(--paper)" stroke-width="1.4"/>
        </svg>
        lpettibone@galavoyant.com
      </li>
      <li>
        <svg viewBox="0 0 20 20" aria-hidden="true">
          <circle cx="10" cy="10" r="8" fill="var(--teal)"/>
          <ellipse cx="10" cy="10" rx="3.5" ry="8" fill="none" stroke="var(--paper)" stroke-width="1.2"/>
          <line x1="2" y1="10" x2="18" y2="10" stroke="var(--paper)" stroke-width="1.2"/>
        </svg>
        www.galavoyant.com
      </li>
    </ul>

    <div class="back-brand"><span class="mark-dot"></span>galavoyant</div>

    <div class="address-band">PO Box 318, Washington, DC 20019</div>
  </section>

</body>
</html>
```